Redesign of key pages of website

We have a website in development: (You can see the test version here: https://staging.pawvira.ai) We want a redesign of a) the home page, b) the set up screens (all four steps), c) the account home page, and the chat page (all four linked below). It needs to look amazing in both desktop and mobile. Also, the chat page needs to have a few different versions to give people a choice between them.

Four areas:
1) Home page: https://staging.pawvira.ai/
2) Account pages: https://staging.pawvira.ai/account/chatsettings.php?step=1
3) Account home page (you'll need to set up an account which is free): https://staging.pawvira.ai/account/summary.php
4) Chat page: https://staging.pawvira.ai/chat.php?id=375

Also to clarify re: code, I don't need any of the interaction/behavior code. I just need the basic HTML and stylesheets so I can integrate that into the existing website.

Please feel free to pass by early versions to me or if you have any clarifications, let me know!

Industry/Entity Type

small businesses

Coding

Coded - Design and coding required

Number of Pages Required

5+ page

Font styles to use
Other font styles liked:
• keep the current font.

Requirements
Must have
• All the same elements/functionality on the current site. Just want a redesign. Also keep the dog visual. Also must work great in mobile and desktop and be really fun and modern and easy.
Nice to have
• Also in the setup pages, need a much better form of navigation (currently just have four circles.)

```html
<!DOCTYPE html>
<html lang="en">
<head>
<meta charset="utf-8">
<title>Pawvira – Home</title>
<link href="https://fonts.googleapis.com/css2?family=Lexend:wght@300;400;500;700&display=swap" rel="stylesheet">
<style>
:root{
  --teal:#14b3a4;
  --teal-soft:#d9f3ef;
  --coral:#f46a6a;
  --coral-soft:#ffd9d8;
  --blue:#3e7bef;
  --blue-deep:#2f6ae6;
  --blue-card:#e6edfd;
  --ink:#333840;
  --muted:#6b7280;
  --white:#ffffff;
}
*{box-sizing:border-box;margin:0;padding:0}
html,body{width:1200px;height:3196px;overflow:hidden}
body{font-family:"Lexend",sans-serif;color:var(--ink);background:var(--white);position:relative}
.abs{position:absolute}
.btn{display:inline-block;background:var(--teal);color:var(--white);font-size:12px;font-weight:500;letter-spacing:1.5px;text-transform:uppercase;padding:12px 26px;border-radius:22px}
.wordmark{font-weight:500;font-size:40px;color:var(--teal);letter-spacing:0}
.dot{width:26px;height:26px;border-radius:50%;background:var(--coral-soft)}

/* header */
.site-header{top:0;left:0;width:1200px;height:96px}
.site-header .wordmark{left:0;width:1200px;text-align:center;top:22px}
.site-header .social{top:36px;left:232px;display:flex;gap:14px}
.site-header .account-dot{top:36px;left:808px}
.site-header .btn{top:32px;left:850px;background:var(--coral);padding:9px 22px;font-size:10px}

/* hero */
.hero-blob-left{left:-60px;top:250px;width:360px;height:360px;border-radius:50%;background:var(--coral-soft)}
.hero-blob-right{right:-40px;top:280px;width:340px;height:340px;border-radius:50%;background:var(--coral-soft)}
.hero-dog-left{left:20px;top:300px;width:260px;height:240px;border-radius:46% 46% 40% 40%;background:linear-gradient(160deg,#8fb0f7,#4f7fe9)}
.hero-dog-right{left:900px;top:300px;width:260px;height:240px;border-radius:46% 46% 40% 40%;background:linear-gradient(200deg,#8fb0f7,#4f7fe9)}
.hero-title{top:180px;left:0;width:1200px;text-align:center;font-size:112px;font-weight:400;letter-spacing:-2px}
.hero-rule{top:320px;left:540px;width:120px;height:3px;background:var(--teal)}
.hero-sub{top:340px;left:0;width:1200px;text-align:center;font-size:15px;line-height:22px;color:var(--muted)}
.hero-actions{top:430px;left:0;width:1200px;display:flex;justify-content:center;gap:30px}

/* features */
.feature-icon{width:46px;height:40px;border-radius:8px}
.feature-title{font-size:58px;font-weight:400;line-height:64px;letter-spacing:-1px}
.feature-text{font-size:13px;line-height:20px;color:var(--muted);width:300px}

.customize-blob{left:660px;top:838px;width:560px;height:300px;background:var(--teal-soft);border-radius:28px 0 0 28px}
.customize-accent{left:1040px;top:1000px;width:220px;height:220px;border-radius:50%;background:var(--teal)}
.customize-icon{left:192px;top:906px;background:var(--teal)}
.customize-title{left:192px;top:958px}
.customize-text{left:196px;top:1098px}

.laptop{left:590px;top:920px;width:420px;height:260px}
.laptop-screen{position:absolute;left:20px;top:0;width:380px;height:240px;background:var(--white);border:8px solid #2b2f36;border-radius:10px 10px 0 0;padding:16px}
.laptop-base{position:absolute;left:0;top:238px;width:420px;height:14px;background:#c9ccd2;border-radius:0 0 10px 10px}
.chat-head{display:flex;gap:12px;align-items:center}
.chat-avatar{width:46px;height:46px;border-radius:50%;background:#f6c6a6}
.chat-name{font-size:14px;font-weight:500}
.chat-role{font-size:9px;color:var(--muted)}
.chat-links{display:flex;gap:8px;margin:10px 0 0 58px}
.chat-links span{width:12px;height:12px;border-radius:50%;background:#9aa3af}
.chat-msg{margin-top:18px;display:flex;gap:8px}
.chat-msg .mini{width:22px;height:22px;border-radius:50%;background:var(--blue)}
.chat-bubble{background:#f1f3f6;border-radius:10px;padding:8px 12px;font-size:9px;line-height:13px;width:220px}

.qualify-blob{left:0;top:1350px;width:545px;height:410px;background:var(--coral-soft);border-radius:0 30px 30px 0}
.qualify-accent{left:-70px;top:1350px;width:160px;height:160px;border-radius:50%;background:var(--coral)}
.qualify-icon{left:686px;top:1414px;background:var(--coral)}
.qualify-title{left:684px;top:1464px}
.qualify-text{left:688px;top:1610px}

.tablet{left:140px;top:1392px;width:440px;height:320px;background:#2b2f36;border-radius:26px;padding:16px}
.calendar{width:100%;height:100%;background:var(--white);border-radius:12px;padding:16px 18px;position:relative}
.cal-title{font-size:14px;font-weight:500}
.cal-month{font-size:11px;margin:14px 0 0 80px}
.cal-grid{display:grid;grid-template-columns:repeat(7,28px);gap:8px 6px;margin-top:14px;font-size:10px;text-align:center}
.cal-grid .wd{font-size:8px;color:var(--muted)}
.cal-grid .av{background:var(--blue-card);color:var(--blue);border-radius:50%;line-height:28px}
.cal-grid .sel{background:var(--blue);color:var(--white);border-radius:50%;line-height:28px}
.cal-grid .dd{line-height:28px;color:#9aa3af}
.slots{position:absolute;right:18px;top:70px;display:flex;flex-direction:column;gap:12px}
.slots span{border:1px solid var(--blue);color:var(--blue);font-size:9px;padding:7px 16px;border-radius:4px}

.manage-blob{left:760px;top:1868px;width:440px;height:410px;background:var(--teal-soft);border-radius:30px 0 0 30px}
.manage-accent{left:1110px;top:2180px;width:180px;height:180px;border-radius:50%;background:var(--teal)}
.manage-icon{left:192px;top:1944px;background:var(--teal)}
.manage-title{left:192px;top:1996px}
.manage-text{left:196px;top:2156px}

.leads-window{left:572px;top:1960px;width:440px;height:300px;background:var(--white);border-radius:6px;box-shadow:0 10px 30px rgba(0,0,0,.12);overflow:hidden}
.leads-bar{height:22px;background:#eef0f3;display:flex;gap:6px;align-items:center;padding-left:10px}
.leads-bar span{width:8px;height:8px;border-radius:50%;background:#c4c8cf}
.leads-head{display:grid;grid-template-columns:1fr 1fr;background:var(--teal);color:var(--white);font-size:10px;padding:6px 12px}
.leads-body{display:grid;grid-template-columns:1fr 1fr;font-size:8px;color:var(--muted);padding:12px;gap:8px 12px;line-height:12px}

/* closing */
.closing-dog{left:468px;top:2380px;width:264px;height:230px;border-radius:46% 46% 40% 40%;background:linear-gradient(180deg,#8fb0f7,#4f7fe9)}
.closing-wave{left:0;top:2560px;width:1200px;height:636px}
.cta-card{left:196px;top:2574px;width:808px;height:290px;background:var(--blue-card);border-radius:14px;text-align:center;padding-top:50px}
.cta-title{font-size:52px;font-weight:400;line-height:62px;color:var(--ink)}
.cta-card .btn{margin-top:26px}
.footer-wordmark{top:2934px;left:0;width:1200px;text-align:center;color:var(--white)}
.feedback{top:3006px;left:0;width:1200px;display:flex;justify-content:center;align-items:center;gap:10px;color:var(--white);font-size:13px}
.feedback i{width:18px;height:18px;border-radius:50%;background:rgba(255,255,255,.5)}
.footer-rule{top:3112px;left:196px;width:808px;height:1px;background:rgba(255,255,255,.4)}
.copyright{top:3128px;left:196px;color:var(--white);font-size:11px}
.footer-social{top:3126px;left:906px;display:flex;gap:8px}
.footer-social span{width:18px;height:18px;border-radius:50%;background:var(--white)}
</style>
</head>
<body>

<header class="site-header abs">
  <div class="social abs"><span class="dot"></span><span class="dot"></span></div>
  <div class="wordmark abs">Pawvira</div>
  <span class="dot account-dot abs"></span>
  <span class="btn abs">Register Now</span>
</header>

<section class="hero">
  <div class="hero-blob-left abs"></div>
  <div class="hero-blob-right abs"></div>
  <div class="hero-dog-left abs" role="img" aria-label="Blue cartoon dog mascot peeking in from the left"></div>
  <div class="hero-dog-right abs" role="img" aria-label="Blue cartoon dog mascot peeking in from the right"></div>
  <h1 class="hero-title abs">Welcome!</h1>
  <div class="hero-rule abs"></div>
  <p class="hero-sub abs">Miri Talks To Your Leads, Qualifies Them, And Gets<br>Them On Your Calendar.</p>
  <div class="hero-actions abs"><span class="btn">Set Up Example</span><span class="btn">Create Your Miri Now</span></div>
</section>

<section class="feature-customize">
  <div class="customize-blob abs"></div>
  <div class="customize-accent abs"></div>
  <div class="feature-icon customize-icon abs"></div>
  <h2 class="feature-title customize-title abs">Customize<br>And Share</h2>
  <p class="feature-text customize-text abs">Miri Talks To Your Leads, Qualifies Them, And Gets Them On Your Calendar.</p>
  <div class="laptop abs">
    <div class="laptop-screen">
      <div class="chat-head"><span class="chat-avatar"></span><div><div class="chat-name">Nora Vale</div><div class="chat-role">Hair Stylist &amp; Owner</div></div></div>
      <div class="chat-links"><span></span><span></span><span></span><span></span></div>
      <div class="chat-msg"><span class="mini"></span><div class="chat-bubble">Hi! I'm Miri, Nora's assistant.<br>How did you hear about Nora?</div></div>
    </div>
    <div class="laptop-base"></div>
  </div>
</section>

<section class="feature-qualify">
  <div class="qualify-blob abs"></div>
  <div class="qualify-accent abs"></div>
  <div class="tablet abs">
    <div class="calendar">
      <div class="cal-title">Select a Date &amp; Time</div>
      <div class="cal-month">June 2023</div>
      <div class="cal-grid">
        <span class="wd">MON</span><span class="wd">TUE</span><span class="wd">WED</span><span class="wd">THU</span><span class="wd">FRI</span><span class="wd">SAT</span><span class="wd">SUN</span>
        <span></span><span></span><span></span><span class="av">1</span><span class="av">2</span><span class="dd">3</span><span class="dd">4</span>
        <span class="av">5</span><span class="av">6</span><span class="av">7</span><span class="av">8</span><span class="av">9</span><span class="dd">10</span><span class="dd">11</span>
        <span class="av">12</span><span class="av">13</span><span class="sel">14</span><span class="av">15</span><span class="av">16</span><span class="dd">17</span><span class="dd">18</span>
        <span class="av">19</span><span class="av">20</span><span class="av">21</span><span class="av">22</span><span class="av">23</span><span class="dd">24</span><span class="dd">25</span>
      </div>
      <div class="slots"><span>10:00am</span><span>11:00am</span><span>12:00pm</span></div>
    </div>
  </div>
  <div class="feature-icon qualify-icon abs"></div>
  <h2 class="feature-title qualify-title abs">Qualify And<br>Schedule</h2>
  <p class="feature-text qualify-text abs">Get The Information You Need From Your Customers. When They Meet Your Criteria, They Can Book A Meeting Directly On Your Calendar.</p>
</section>

<section class="feature-manage">
  <div class="manage-blob abs"></div>
  <div class="manage-accent abs"></div>
  <div class="feature-icon manage-icon abs"></div>
  <h2 class="feature-title manage-title abs">Manage<br>Your Leads</h2>
  <p class="feature-text manage-text abs">Get Notified Via Email Or Text. See A Summary Of Each Lead And Manage Them In One Place. Search, Sort, Add Notes, And More.</p>
  <div class="leads-window abs">
    <div class="leads-bar"><span></span><span></span><span></span></div>
    <div class="leads-head"><span>Summary</span><span>Email</span></div>
    <div class="leads-body">
      <span>Interested in a fitness class. Prefers weekday mornings.</span><span>jordan@mail.test</span>
      <span>Wants a cut and color. Booked for next Tuesday.</span><span>casey@mail.test</span>
      <span>Asked about pricing and a free first visit.</span><span>riley@mail.test</span>
    </div>
  </div>
</section>

<section class="closing">
  <svg class="closing-wave abs" viewBox="0 0 1200 636" preserveAspectRatio="none" aria-hidden="true">
    <path d="M0 120 C300 40 700 200 1200 80 L1200 636 L0 636 Z" fill="var(--blue)"/>
    <circle cx="110" cy="460" r="90" fill="var(--blue-deep)"/>
    <circle cx="1100" cy="380" r="70" fill="var(--blue-deep)"/>
  </svg>
  <div class="closing-dog abs" role="img" aria-label="Blue cartoon dog mascot resting on the card"></div>
  <div class="cta-card abs">
    <h2 class="cta-title">Let Miri Handle Your<br>Leads Today!</h2>
    <span class="btn">Create Your Miri Now</span>
  </div>
  <div class="wordmark footer-wordmark abs">Pawvira</div>
  <div class="feedback abs"><i></i>Have Feedback? Let Us Know</div>
  <div class="footer-rule abs"></div>
  <p class="copyright abs">© 2021 Pawvira.AI. All Rights Reserved. Terms Of Use</p>
  <div class="footer-social abs"><span></span><span></span><span></span><span></span></div>
</section>

</body>
</html>
```